psd/html for a e wallet payment website designed

hi
i am in need of a psd / html for a whole website designed
the site is a e wallet /payment system i can i will provide a link to what type of style i am looking for but i can not stress this enough i do not want anyone replicating the website i am just providing the links to show you what kind of function and the content that is involved also, i have a srs with detailed pages you can read and refer to if need be
thanks of viewing
Vantoleaf.com
Brisklune.com
marblequivercoin.com
Qrdelivane.com

```html
<!DOCTYPE html>
<html lang="en">
<head>
<meta charset="utf-8">
<title>Secure wallet Payment</title>
<link href="https://fonts.googleapis.com/css2?family=Questrial&family=Arimo:wght@400;700&family=Open+Sans:wght@400&family=Courier+Prime&display=swap" rel="stylesheet">
<style>
:root{
  --blue:#0a78ad;
  --blue-bright:#1f8fd6;
  --blue-band:#0b78a8;
  --ink:#333;
  --muted:#777;
  --line:#d9d9d9;
  --red:#c8141e;
  --orange:#f58a07;
  --panel:#f1f1f1;
  --placeholder:#e4e4e4;
}
*{margin:0;padding:0;box-sizing:border-box}
html,body{width:960px;height:1200px;overflow:hidden;background:#fff}
body{position:relative;font-family:Arimo,Arial,sans-serif;color:var(--ink)}
.abs{position:absolute}
.top-rule{left:0;top:0;width:960px;height:2px;background:var(--blue-bright)}
.account-tab{left:781px;top:0;width:97px;height:20px;background:var(--blue-bright);color:#fff;font-size:10px;text-align:center;line-height:20px;border-radius:0 0 6px 6px}
.brand{left:91px;top:26px;font-family:Questrial,sans-serif;font-size:31px;letter-spacing:2px;color:#333}
.social{top:61px;display:flex;gap:9px}
.social span{width:18px;height:18px;border-radius:2px;display:block;background:#c9c9c9}
.band{left:0;top:90px;width:960px;height:377px;background:var(--blue-band)}
.nav{left:95px;top:98px;display:flex;font-family:Questrial,sans-serif;font-size:12.5px;letter-spacing:.5px;color:#fff}
.nav a{color:#fff;text-decoration:none;height:28px;line-height:28px;padding:0 15px}
.nav a.current{background:#e8e8e8;color:#333;border-radius:3px}
.hero{left:98px;top:137px;width:748px;height:315px;background:#fff;border-radius:5px;box-shadow:0 0 0 1px #d6e4ec}
.hero-photo{left:6px;top:5px;width:420px;height:305px;background:linear-gradient(90deg,#e6dcd3 0%,#fff 100%)}
.hero-strip{left:152px;top:21px;width:590px;height:83px;background:linear-gradient(90deg,#eef5f3 0%,#cfe5df 50%,#9fcbbd 100%);font-family:"Open Sans",sans-serif;font-size:19px;color:#222;text-align:right;padding:30px 14px 0 0}
.hero h2{left:382px;top:126px;font-family:Questrial,sans-serif;font-size:26px;letter-spacing:2px;color:var(--blue-bright);font-weight:700}
.hero p{left:384px;top:165px;width:350px;font-family:Questrial,sans-serif;font-size:11.5px;line-height:19px;letter-spacing:.9px;color:#444}
.btn-signup{left:593px;top:253px;width:123px;height:36px;border-radius:4px;background:linear-gradient(#1e9ae0,#0a6fb5);border:1px solid #0a5c98;color:#fff;font-family:Questrial,sans-serif;font-weight:700;font-size:15px;letter-spacing:1px;text-align:center;line-height:34px}
.tabs{left:0;top:467px;width:960px;height:80px;border-bottom:1px solid var(--line)}
.tab{position:absolute;top:0;height:79px}
.tab.active{background:#f0f0f0}
.tab h3{position:absolute;font-family:Questrial,sans-serif;font-size:20px;letter-spacing:1.5px;color:var(--blue-bright);font-weight:700}
.tab small{position:absolute;font-family:Questrial,sans-serif;font-size:10px;letter-spacing:.5px;color:#888}
.tab svg{position:absolute}
.about-title{left:0;top:567px;width:960px;text-align:center;font-family:Questrial,sans-serif;font-size:20px;letter-spacing:1.5px;font-weight:700;color:#444}
.about-text{left:95px;top:601px;width:770px;text-align:center;font-family:Questrial,sans-serif;font-size:14px;line-height:19px;letter-spacing:.9px;color:#333}
.features-title{left:99px;top:694px;font-family:Questrial,sans-serif;font-size:20px;font-weight:700;letter-spacing:1.5px;color:var(--blue-bright)}
.features-rule{left:95px;top:732px;width:487px;height:1px;background:#ccc}
.feature{position:absolute;width:152px;font-size:10px;line-height:14.5px;color:#333;letter-spacing:.2px;text-align:justify}
.feature b{display:block;font-size:11px;margin-bottom:1px;text-align:left}
.feature a{display:block;color:var(--red);text-decoration:none;margin-top:2px;text-align:left}
.dots-v{left:341px;top:745px;height:223px;border-left:1px dotted #aaa}
.dots-h1{left:92px;top:849px;width:224px;border-top:1px dotted #aaa}
.dots-h2{left:365px;top:849px;width:224px;border-top:1px dotted #aaa}
.sidebar{left:624px;top:690px;width:246px;height:303px;background:var(--panel);border-radius:8px}
.ad-sellers{left:16px;top:9px;width:216px;height:135px;background:#fff;border:1px solid #aaa;border-radius:8px;overflow:hidden}
.ad-person{left:10px;top:6px;width:88px;height:106px;background:var(--placeholder);border-radius:6px}
.ad-copy{left:102px;top:27px;width:112px;text-align:center;font-family:"Courier Prime",monospace;font-size:9.5px;line-height:10.8px;color:#d4350c}
.ad-btn{left:18px;top:115px;width:95px;height:14px;background:#666;border-radius:3px;color:#fff;font-family:"Courier Prime",monospace;font-size:8px;text-align:center;line-height:14px}
.badge{top:117px;width:24px;height:12px;background:#d6d6d6;border-radius:2px}
.ad-cards{left:12px;top:163px;width:222px;height:128px;background:#fff;border:2px solid #e8e8e8}
.ad-cards-img{left:0;top:0;width:218px;height:74px;background:linear-gradient(180deg,#c9d6ee,#eef2f8)}
.ad-cards-text{left:0;top:84px;width:218px;text-align:center;font-family:Questrial,sans-serif;font-size:22px;letter-spacing:-1px;color:#222}
.footer-rule{left:0;top:1013px;width:960px;height:2px;background:#e6e6e6}
.foot-h{font-family:Arimo,sans-serif;font-size:13px;color:#222}
.foot-line{height:1px;background:#e0e0e0}
.foot-list{list-style:none;font-size:9.5px;color:#666;letter-spacing:.4px}
.foot-list li{height:19.2px}
.foot-list li::before{content:"›";margin-right:8px;color:#999}
.contact{font-size:9.5px;color:#444;letter-spacing:.3px;line-height:11px}
.field{position:absolute;left:534px;width:177px;background:#f0f0f0;border-radius:4px;font-size:9.5px;color:#444;padding:4px 8px}
.btn-send{left:638px;top:1133px;width:67px;height:18px;border-radius:9px;background:linear-gradient(#ffa832,#f07c00);color:#fff;font-size:11px;font-weight:700;text-align:center;line-height:18px}
.foot-mark{left:759px;top:1036px;width:77px;height:56px;background:#1487d6;border-radius:2px}
.foot-brand{left:740px;top:1098px;width:120px;text-align:center;font-family:Questrial,sans-serif;font-size:17px;letter-spacing:2.5px;line-height:16px;color:#333}
.bottom-bar{left:0;top:1162px;width:960px;height:4px;background:var(--blue-bright)}
.copyright{left:85px;top:1176px;font-size:10px;color:#444}
.follow{left:745px;top:1178px;font-size:9px;color:#444;display:flex;gap:3px;align-items:center}
.follow span{width:13px;height:13px;display:block;border-radius:2px;background:#c9c9c9}
</style>
</head>
<body>
<div class="abs top-rule"></div>
<div class="abs account-tab">Creat Account ?</div>
<div class="abs brand">Secure wallet Payment</div>
<div class="abs social" style="left:766px"><span></span><span></span><span></span><span></span></div>

<div class="abs band"></div>
<nav class="abs nav">
  <a class="current">Home</a>
  <a style="margin-left:18px">Personal Accounts</a>
  <a style="margin-left:25px">Business Accounts</a>
  <a style="margin-left:25px">Beginner's Guide</a>
  <a style="margin-left:18px">Developers</a>
  <a style="margin-left:17px">Help Centre</a>
</nav>

<section class="abs hero">
  <div class="abs hero-photo" role="img" aria-label="Photo of a woman on the phone holding a payment card"></div>
  <div class="abs hero-strip">we ensure that your business is online and accepting payments</div>
  <h2 class="abs">Exclusive Card Products</h2>
  <p class="abs">Efficient and professional support available via phone, live chat and our exclusive ticket/knowledgebase area. Get the help you need, when you need it.</p>
  <div class="abs btn-signup">Sign up Now</div>
</section>

<section class="abs tabs">
  <div class="tab active" style="left:82px;width:240px">
    <svg width="38" height="38" style="left:18px;top:17px" viewBox="0 0 38 38"><circle cx="19" cy="19" r="17" fill="#9a9a9a"/><circle cx="15" cy="14" r="9" fill="#e8e8e8"/><circle cx="19" cy="19" r="17" fill="none" stroke="#666" stroke-width="1.5"/></svg>
    <h3 style="left:71px;top:24px">Buy Online</h3>
    <small style="left:71px;top:48px">Payments to others are instant</small>
  </div>
  <div class="tab" style="left:322px;width:284px">
    <svg width="38" height="38" style="left:26px;top:20px" viewBox="0 0 38 38"><g fill="#aaa"><rect x="16" y="0" width="6" height="38" rx="1"/><rect x="0" y="16" width="38" height="6" rx="1"/><rect x="16" y="0" width="6" height="38" rx="1" transform="rotate(45 19 19)"/><rect x="16" y="0" width="6" height="38" rx="1" transform="rotate(-45 19 19)"/></g><circle cx="19" cy="19" r="13" fill="#bbb"/><circle cx="19" cy="19" r="6" fill="#fff" stroke="#888" stroke-width="2"/></svg>
    <h3 style="left:76px;top:22px">SELL Online</h3>
    <small style="left:76px;top:46px">Payments to others are instant</small>
  </div>
  <div class="tab" style="left:606px;width:354px;border-left:1px solid #eee">
    <svg width="40" height="36" style="left:19px;top:18px" viewBox="0 0 40 36"><path d="M2 2h36v24H16l-8 8v-8H2z" fill="#ddd" stroke="#bbb"/><circle cx="13" cy="14" r="1.6" fill="#888"/><circle cx="20" cy="14" r="1.6" fill="#888"/><circle cx="27" cy="14" r="1.6" fill="#888"/></svg>
    <h3 style="left:75px;top:20px">How It Works</h3>
    <small style="left:75px;top:44px">Payments to others are instant</small>
  </div>
</section>

<h2 class="abs about-title">About Secure Wallet Payment</h2>
<p class="abs about-text">Whether you're a traditional brick-and-mortar looking to expand online, or a new business venture seeking the most convenient way to develop or enhance your web presence, Brisklune's complete suite of customizable business tools will help your business thrive in today's evolution-Commerce.</p>

<h2 class="abs features-title">Features</h2>
<div class="abs features-rule"></div>

<svg class="abs" style="left:100px;top:742px" width="64" height="70" viewBox="0 0 64 70"><rect x="2" y="26" width="16" height="36" fill="#f5a000"/><rect x="21" y="2" width="16" height="60" fill="#2d7be0"/><rect x="40" y="16" width="16" height="46" fill="#57b530"/><circle cx="37" cy="48" r="10" fill="#fff" stroke="#bbb" stroke-width="3"/><path d="M45 56l7 7" stroke="#c00" stroke-width="4"/></svg>
<div class="feature" style="left:173px;top:751px"><b>Instant transactions</b>search engine to locate a product or service, that engine attempts to guide the user...<a>More info [+]</a></div>

<svg class="abs" style="left:365px;top:757px" width="68" height="60" viewBox="0 0 68 60"><path d="M6 16L48 2l4 12z" fill="#333"/><rect x="2" y="14" width="60" height="44" rx="6" fill="#333"/><rect x="36" y="26" width="30" height="18" rx="5" fill="#fff"/><rect x="40" y="30" width="22" height="10" rx="4" fill="#333"/><circle cx="46" cy="35" r="3" fill="#fff"/></svg>
<div class="feature" style="left:446px;top:751px"><b>Multiple wallets</b>search engine to locate a product or service, that engine attempts to guide the user...<a>More info [+]</a></div>

<div class="abs dots-v"></div><div class="abs dots-h1"></div><div class="abs dots-h2"></div>

<svg class="abs" style="left:100px;top:882px" width="64" height="54" viewBox="0 0 64 54"><path d="M20 20L30 2M44 20L34 2" stroke="#222" stroke-width="4" fill="none"/><rect x="2" y="18" width="60" height="7" rx="3" fill="#222"/><path d="M6 27h52l-5 25H11z" fill="#222"/><g stroke="#fff" stroke-width="3"><path d="M18 32v15M26 32v15M34 32v15M42 32v15M50 32v15"/></g></svg>
<div class="feature" style="left:173px;top:873px"><b>Shopping Online</b>search engine to locate a product or service, that engine attempts to guide the user...<a>More info [+]</a></div>

<svg class="abs" style="left:368px;top:882px" width="62" height="56" viewBox="0 0 62 56"><rect x="6" y="0" width="50" height="5" fill="#222"/><path d="M2 8h58v10H2z" fill="#222"/><rect x="6" y="20" width="50" height="34" fill="#222"/><rect x="12" y="26" width="20" height="16" fill="#fff"/><rect x="38" y="28" width="12" height="26" fill="#fff"/></svg>
<div class="feature" style="left:446px;top:873px"><b>Selling Online</b>search engine to locate a product or service, that engine attempts to guide the user...<a>More info [+]</a></div>

<aside class="abs sidebar">
  <div class="abs ad-sellers">
    <div class="abs ad-person" role="img" aria-label="Illustration of a woman sitting with a laptop"></div>
    <div class="abs ad-copy">Enable Online Sellers to accept payments safely and easily in more than 10 major foreign currencies</div>
    <div class="abs ad-btn">Click For More Info</div>
    <div class="abs badge" style="left:144px"></div><div class="abs badge" style="left:174px"></div>
  </div>
  <div class="abs ad-cards">
    <div class="abs ad-cards-img" role="img" aria-label="Photo of fanned payment cards"></div>
    <div class="abs ad-cards-text">ONLINE PAYMENT</div>
  </div>
</aside>

<div class="abs footer-rule"></div>

<div class="abs foot-h" style="left:94px;top:1028px">Navigation</div>
<div class="abs foot-line" style="left:94px;top:1048px;width:176px"></div>
<ul class="abs foot-list" style="left:94px;top:1057px"><li>Home</li><li>Who We Are?</li><li>What We Do?</li><li>Products</li><li>News Blog</li></ul>
<ul class="abs foot-list" style="left:197px;top:1057px"><li>Contact</li><li>Site Map</li><li>Terms</li><li>Privacy Policy</li></ul>

<div class="abs foot-h" style="left:319px;top:1028px">Contact Info</div>
<div class="abs foot-line" style="left:319px;top:1048px;width:176px"></div>
<div class="abs contact" style="left:320px;top:1057px"><i>Secure wallet Payment</i><br><br>48 Harlow Quay, 2nd Floor<br>Denmore, OR 97321</div>
<div class="abs contact" style="left:319px;top:1105px;font-size:11px;font-weight:700;color:#555">(555)-014-PAYS (7297)</div>
<div class="abs contact" style="left:322px;top:1124px;font-family:Questrial,sans-serif;font-size:10.5px;letter-spacing:.8px">Secure wallet Payment</div>

<div class="abs foot-h" style="left:532px;top:1028px">Get in Touch</div>
<div class="abs foot-line" style="left:532px;top:1048px;width:176px"></div>
<div class="field" style="top:1055px;height:19px">Name</div>
<div class="field" style="top:1077px;height:19px">Emai</div>
<div class="field" style="top:1100px;height:28px">Comments</div>
<div class="abs btn-send">Send</div>

<div class="abs foot-mark"></div>
<div class="abs foot-brand">Secure<br>wallet<br>Payment</div>

<div class="abs bottom-bar"></div>
<div class="abs copyright">© 2013 Vantoleaf Secure wallet Payment</div>
<div class="abs follow">Follow us&nbsp;&nbsp;<span></span><span></span><span></span><span></span><span></span></div>
</body>
</html>
```